Refrigeration & Air Conditioning modern and appealing

We want to design a business card that is modern and appealing using existing logo supplied

Front card
Residential Commercial Diary
RTA : AU052731
Licence L287456

Back card
Warren Kostig
Director
0491 357 208
info@frostlinerefrigeration.com.au
www.frostlinerefrigeration.com.au
• Air Conditioning
• Cool Rooms & Refrigeration
• Installation
• Service & Repair
• Preventative Maintenance

We offer 24/7 emergency service

```html
<!DOCTYPE html>
<html lang="en">
<head>
<meta charset="utf-8">
<title>Frostline Refrigeration &amp; Air Conditioning – Business Card</title>
<link href="https://fonts.googleapis.com/css2?family=Montserrat:wght@400;500;700&display=swap" rel="stylesheet">
<style>
  :root {
    --bg: #2a2a2b;
    --card: #141315;
    --purple: #9361cc;
    --white: #f4f2f6;
    --muted: #d9d4de;
  }
  * { margin: 0; padding: 0; box-sizing: border-box; }
  html, body { width: 1200px; height: 875px; overflow: hidden; }
  body {
    background: var(--bg);
    font-family: "Montserrat", sans-serif;
    display: flex; align-items: center; justify-content: center; gap: 40px;
  }
  .card {
    width: 540px; height: 309px;
    background: var(--card);
    border-radius: 16px;
    position: relative;
    color: var(--white);
  }
  .brand {
    display: flex; align-items: center; gap: 12px;
    font-weight: 700; letter-spacing: 2px; color: var(--white);
  }
  .brand-dot { border-radius: 50%; background: var(--purple); }

  /* Front */
  .card-front .brand { position: absolute; left: 0; right: 0; top: 110px; justify-content: center; font-size: 46px; }
  .card-front .brand-dot { width: 40px; height: 40px; }
  .card-front .credentials {
    position: absolute; left: 0; right: 0; top: 200px;
    text-align: center; font-size: 13px; font-weight: 500; color: var(--white);
  }
  .credentials .sep { display: inline-block; width: 1px; height: 14px; background: var(--white); margin: 0 8px; vertical-align: middle; }

  /* Back */
  .card-back .brand { position: absolute; right: 32px; top: 34px; font-size: 28px; }
  .card-back .brand-dot { width: 26px; height: 26px; }
  .person { position: absolute; left: 32px; top: 80px; }
  .person-name { font-size: 20px; font-weight: 700; color: var(--purple); }
  .person-role { font-size: 12px; color: var(--muted); margin-top: 2px; }
  .divider { position: absolute; left: 32px; right: 32px; top: 128px; height: 1.5px; background: var(--purple); }
  .contacts { position: absolute; left: 32px; top: 148px; list-style: none; }
  .contacts li { display: flex; align-items: center; gap: 9px; font-size: 11.5px; color: var(--muted); margin-bottom: 9px; }
  .contacts svg { width: 12px; height: 12px; fill: var(--purple); flex: none; }
  .tagline { position: absolute; left: 32px; bottom: 30px; font-size: 12.5px; font-weight: 700; color: var(--purple); }
  .services { position: absolute; right: 32px; top: 148px; list-style: none; text-align: right; }
  .services li { font-size: 11.5px; color: var(--muted); margin-bottom: 7px; display: flex; justify-content: flex-end; align-items: center; gap: 8px; }
  .services li::after { content: ""; width: 6px; height: 6px; border-radius: 50%; background: var(--purple); }
</style>
</head>
<body>
  <section class="card card-front">
    <div class="brand"><span class="brand-dot"></span>FROSTLINE</div>
    <p class="credentials">RTA : AU052731<span class="sep"></span>Licence L287456</p>
  </section>

  <section class="card card-back">
    <div class="brand"><span class="brand-dot"></span>FROSTLINE</div>
    <div class="person">
      <p class="person-name">Warren Kostig</p>
      <p class="person-role">Director</p>
    </div>
    <div class="divider"></div>
    <ul class="contacts">
      <li><svg viewBox="0 0 24 24"><path d="M6.6 10.8a15 15 0 0 0 6.6 6.6l2.2-2.2a1 1 0 0 1 1-.25 11.4 11.4 0 0 0 3.6.57 1 1 0 0 1 1 1V20a1 1 0 0 1-1 1A17 17 0 0 1 3 4a1 1 0 0 1 1-1h3.5a1 1 0 0 1 1 1c0 1.25.2 2.45.57 3.57a1 1 0 0 1-.25 1z"/></svg>0491 357 208</li>
      <li><svg viewBox="0 0 24 24"><path d="M2 5h20v14H2zm2 2v.5l8 5 8-5V7l-8 5z"/></svg>info@frostlinerefrigeration.com.au</li>
      <li><svg viewBox="0 0 24 24"><path d="M12 2a10 10 0 1 0 0 20 10 10 0 0 0 0-20zm6.9 6h-3a15 15 0 0 0-1.3-3.9A8 8 0 0 1 18.9 8zM12 4c.8 1.2 1.5 2.5 1.9 4h-3.8c.4-1.5 1.1-2.8 1.9-4zM4.3 14a8 8 0 0 1 0-4h3.4a16 16 0 0 0 0 4zm.8 2h3a15 15 0 0 0 1.3 3.9A8 8 0 0 1 5.1 16zm3-8h-3a8 8 0 0 1 4.3-3.9A15 15 0 0 0 8.1 8zM12 20c-.8-1.2-1.5-2.5-1.9-4h3.8c-.4 1.5-1.1 2.8-1.9 4zm2.3-6H9.7a14 14 0 0 1 0-4h4.6a14 14 0 0 1 0 4zm.3 5.9a15 15 0 0 0 1.3-3.9h3a8 8 0 0 1-4.3 3.9zm1.7-5.9a16 16 0 0 0 0-4h3.4a8 8 0 0 1 0 4z"/></svg>www.frostlinerefrigeration.com.au</li>
    </ul>
    <ul class="services">
      <li>Air Conditioning</li>
      <li>Cool Rooms &amp; Refrigeration</li>
      <li>Installation</li>
      <li>Service &amp; Repair</li>
      <li>Preventative Maintenance</li>
    </ul>
    <p class="tagline">We offer 24/7 emergency service</p>
  </section>
</body>
</html>
```